Cordova Exercise Phone Application Screen Design

We need a sharp professional design for a phone application. We specialize in Health and Fitness Software. This app will be a companion for www.VigorDeckNow.com.
We will be doing all backend and javascript work here and we need someone to create the HTML and CSS for the application which will be developed in Cordova.
For the contest we are submitting three screens. Once we award a winner we will give the winner the first oportunity to bid on the remaining 10 screens.
For the first step of the contest please do the page 1 and page 2 screen design, feel free to submit multiple designs. If we like your designs we will contact you and ask you to design the third page. Once that is done we would like to see the HTML and CSS for the three pages.
Page 1: Simple Home Page
Page 2: Client Search - The search is at the top and the results are below that. The Active | Inactive section is a selection (see https://quorblenet.com/radio-buttons-as-toggle-buttons-with-css/ for an example). Client A has their record expanded (that is what the triangle is). 136 stars should be 136 with Font-Awesome star after the number. To see what the graphs should look like please see the attached png. Then a list is below the stars and graphs.
Page 3/4: Step 1 of 3 - When the magnifying glass is selected a flyout with the search criteria comes out (page 3). Criteria is selected and the results are shown (page 4).
The default width should be 320 but the application should look good on all phones and tablets.
Please feel free to contact us with questions. The winner will get more work of a similar nature.

Target Market(s)
Physical Therapists
Colors
Designer to choose colors to be used in the design.
Requirements
Must have
- Clean and easy to understand design. Look professional and uncluttered. Be easy to understand and use. Must have the logo at the top (just the VDN logo is fine)
Should not have
- Cartoonish look and feel.

```html
<!DOCTYPE html>
<html lang="en">
<head>
<meta charset="utf-8">
<title>Vigor Deck Now – Home and Client Search</title>
<link rel="stylesheet" href="https://fonts.googleapis.com/css2?family=Roboto:wght@400;500;700&display=swap">
<style>
  :root {
    --canvas: #ffffff;
    --green-top: #2f9a4e;
    --green-bottom: #5cc279;
    --green-text: #3cbf5f;
    --dark-1: #121214;
    --dark-2: #1c1c1e;
    --row-top: #2a2a2c;
    --row-bottom: #1d1d1f;
    --field-border: #4a4a4c;
    --field-text: #7a7a7c;
    --white: #ffffff;
    --line: #0a0a0a;
    --inactive-red: #ff2a2a;
    --badge-red: #e8191e;
    --sub-row: #222224;
  }
  * { box-sizing: border-box; margin: 0; padding: 0; }
  html, body { width: 976px; height: 1200px; overflow: hidden; }
  body {
    background: var(--canvas);
    font-family: "Roboto", sans-serif;
    color: var(--white);
    position: relative;
  }
  .screen {
    position: absolute;
    background: var(--dark-1);
    overflow: hidden;
  }
  .screen--home { left: 131px; top: 261px; width: 310px; height: 620px; }
  .screen--search { left: 552px; top: 268px; width: 313px; height: 606px; }

  .app-header {
    background: linear-gradient(var(--green-top), var(--green-bottom));
    display: flex; align-items: center; justify-content: center;
    border-bottom: 1px solid #1e6e35;
  }
  .screen--home .app-header { height: 64px; }
  .screen--search .app-header { height: 65px; }
  .brand {
    display: flex; align-items: center; gap: 8px;
    font-weight: 700; color: var(--white); letter-spacing: 2px;
  }
  .brand__mark {
    width: 12px; height: 12px; background: var(--white);
  }
  .brand__name { font-size: 20px; }

  .toolbar {
    height: 49px;
    background: linear-gradient(#2c2c2e, #161618);
    display: flex; align-items: center; justify-content: space-between;
    padding: 0 11px;
    border-bottom: 1px solid var(--line);
  }
  .mail-alert { position: relative; width: 18px; height: 14px; }
  .mail-alert__badge {
    position: absolute; left: 10px; top: -8px;
    width: 14px; height: 14px; border-radius: 50%;
    background: var(--badge-red);
    font-size: 9px; font-weight: 700; line-height: 14px; text-align: center;
  }

  .menu { list-style: none; }
  .menu__item {
    height: 84px;
    display: flex; align-items: center;
    padding: 0 17px 0 18px;
    background: linear-gradient(#2b2b2d, #1e1e20);
    border-bottom: 2px solid var(--line);
    font-size: 15px;
  }
  .menu__item--active { background: linear-gradient(var(--green-top), var(--green-bottom)); }
  .menu__icon {
    width: 42px; height: 42px; border-radius: 5px;
    background: #000; display: flex; align-items: center; justify-content: center;
    flex-shrink: 0;
  }
  .menu__item--active .menu__icon { background: var(--white); }
  .menu__label { flex: 1; margin-left: 17px; line-height: 22px; }

  .nav-bar {
    height: 47px;
    background: linear-gradient(#2a2a2c, #161618);
    display: flex; align-items: center; justify-content: space-between;
    padding: 0 11px 0 13px;
    border-bottom: 1px solid var(--line);
  }
  .nav-bar__title { font-size: 16px; font-weight: 500; }

  .search-form {
    padding: 16px 13px 0;
    display: grid; grid-template-columns: 141px 141px; column-gap: 6px; row-gap: 6px;
  }
  .search-field {
    height: 34px;
    border: 1px solid var(--field-border);
    background: var(--dark-2);
    color: var(--field-text);
    font-size: 12px;
    display: flex; align-items: center; justify-content: center;
  }
  .search-actions {
    display: flex; align-items: center; justify-content: space-between;
    padding: 0 13px; margin-top: 7px; height: 36px;
  }
  .status-toggle { font-size: 12px; display: flex; align-items: center; gap: 7px; }
  .status-toggle__active { color: var(--green-text); }
  .status-toggle__divider { color: #888; }
  .status-toggle__inactive { color: var(--inactive-red); }
  .search-button {
    width: 85px; height: 35px; border-radius: 3px;
    background: linear-gradient(var(--green-top), #3aa55a);
    font-size: 12px; font-weight: 700;
    display: flex; align-items: center; justify-content: center;
  }

  .results { margin: 21px 13px 0; width: 285px; font-size: 11px; }
  .results__head {
    height: 46px;
    display: grid; grid-template-columns: 97px 81px 1fr;
    background: linear-gradient(var(--green-top), var(--green-bottom));
    font-size: 13px;
  }
  .results__head span {
    display: flex; align-items: center; padding-left: 11px;
    border-right: 1px solid var(--dark-1);
  }
  .results__head span:first-child { padding-left: 11px; }
  .results__head span:last-child { border-right: 0; }
  .client-row {
    height: 37px;
    display: grid; grid-template-columns: 97px 81px 1fr;
    align-items: center;
    background: linear-gradient(var(--row-top), var(--row-bottom));
    border-bottom: 1px solid var(--line);
  }
  .client-row > span:first-child { padding-left: 11px; }
  .client-row > span:nth-child(2) { padding-left: 14px; }
  .client-dob { display: flex; align-items: center; padding-left: 15px; gap: 8px; }
  .client-dob__toggle { margin-left: auto; margin-right: 9px; }

  .client-detail { background: var(--sub-row); padding-bottom: 6px; border-bottom: 1px solid var(--line); }
  .client-detail__summary {
    height: 23px; display: flex; align-items: center; font-size: 11px;
  }
  .stars { margin-left: 42px; display: flex; align-items: center; gap: 3px; width: 88px; }
  .prescription-head {
    margin: 0 14px 0 16px; height: 33px;
    background: linear-gradient(var(--green-top), var(--green-bottom));
    display: flex; align-items: center; font-size: 12px;
  }
  .prescription-head span:first-child { margin-left: 26px; width: 84px; }
  .prescription-row {
    height: 32px; display: flex; align-items: center;
    margin: 0 14px 0 16px; font-size: 10px;
  }
  .prescription-row > span:first-child { margin-left: 26px; width: 84px; }
  .prescription-row > span:nth-child(2) { width: 70px; }
  .action-select {
    margin-left: auto; width: 75px; height: 25px;
    border: 1px solid var(--field-border); background: var(--dark-1);
    display: flex; align-items: center; justify-content: space-between;
    padding: 0 3px 0 6px; font-size: 9px;
  }
  .action-select__arrow {
    width: 15px; height: 16px; background: var(--white);
    display: flex; align-items: center; justify-content: center;
  }
</style>
</head>
<body>

<section class="screen screen--home" aria-label="Home screen">
  <header class="app-header">
    <div class="brand"><span class="brand__name">VDN VIGOR DECK NOW</span></div>
  </header>
  <div class="toolbar">
    <div class="mail-alert">
      <svg width="17" height="13" viewBox="0 0 17 13"><rect x="0" y="1" width="17" height="12" rx="1" fill="#fff"/><path d="M0 2 L8.5 8 L17 2" stroke="#222" stroke-width="1.3" fill="none"/></svg>
      <span class="mail-alert__badge">2</span>
    </div>
    <svg width="14" height="14" viewBox="0 0 14 14"><circle cx="7" cy="7" r="6" stroke="#fff" stroke-width="1.5" fill="none"/><path d="M5 5.5 a2 2 0 1 1 2.6 1.9 c-.6.3-.6.7-.6 1.3" stroke="#fff" stroke-width="1.5" fill="none"/><circle cx="7" cy="10.5" r=".9" fill="#fff"/></svg>
  </div>
  <ul class="menu">
    <li class="menu__item">
      <span class="menu__icon"><svg width="26" height="26" viewBox="0 0 26 26"><circle cx="10" cy="10" r="7" stroke="#fff" stroke-width="2" fill="none"/><path d="M15 15 L23 23" stroke="#fff" stroke-width="3.5" stroke-linecap="round"/></svg></span>
      <span class="menu__label">Search for Clients/Create Exercise Program</span>
      <svg width="12" height="20" viewBox="0 0 12 20"><path d="M2 2 L10 10 L2 18" stroke="#fff" stroke-width="2" fill="none"/></svg>
    </li>
    <li class="menu__item">
      <span class="menu__icon"><svg width="28" height="28" viewBox="0 0 28 28"><circle cx="12" cy="9" r="6" stroke="#fff" stroke-width="1.6" fill="none"/><path d="M2 25 c0-6 4-9 10-9 2 0 4 .4 5 1" stroke="#fff" stroke-width="1.6" fill="none"/><path d="M21 18 v8 M17 22 h8" stroke="#fff" stroke-width="1.6"/></svg></span>
      <span class="menu__label">Add Client</span>
      <svg width="12" height="20" viewBox="0 0 12 20"><path d="M2 2 L10 10 L2 18" stroke="#fff" stroke-width="2" fill="none"/></svg>
    </li>
    <li class="menu__item menu__item--active">
      <span class="menu__icon"><svg width="26" height="20" viewBox="0 0 26 20"><rect x="1" y="1" width="24" height="18" stroke="#3aa55a" stroke-width="1.8" fill="none"/><path d="M1 1 L13 11 L25 1 M1 19 L10 9 M25 19 L16 9" stroke="#3aa55a" stroke-width="1.8" fill="none"/></svg></span>
      <span class="menu__label">Messages(25)</span>
      <svg width="12" height="20" viewBox="0 0 12 20"><path d="M2 2 L10 10 L2 18" stroke="#fff" stroke-width="2" fill="none"/></svg>
    </li>
    <li class="menu__item">
      <span class="menu__icon"><svg width="30" height="20" viewBox="0 0 30 20"><rect x="1" y="7" width="3" height="6" fill="#fff"/><rect x="5" y="3" width="4" height="14" fill="#fff"/><rect x="9" y="9" width="12" height="2.5" fill="#fff"/><rect x="21" y="3" width="4" height="14" fill="#fff"/><rect x="26" y="7" width="3" height="6" fill="#fff"/></svg></span>
      <span class="menu__label">Protocols</span>
      <svg width="12" height="20" viewBox="0 0 12 20"><path d="M2 2 L10 10 L2 18" stroke="#fff" stroke-width="2" fill="none"/></svg>
    </li>
    <li class="menu__item">
      <span class="menu__icon"><svg width="26" height="26" viewBox="0 0 26 26"><circle cx="13" cy="13" r="4" stroke="#fff" stroke-width="1.6" fill="none"/><path d="M13 2 v4 M13 20 v4 M2 13 h4 M20 13 h4 M5.2 5.2 l2.8 2.8 M18 18 l2.8 2.8 M5.2 20.8 l2.8-2.8 M18 8 l2.8-2.8" stroke="#fff" stroke-width="2.4"/><circle cx="13" cy="13" r="7.5" stroke="#fff" stroke-width="1.6" fill="none"/></svg></span>
      <span class="menu__label">Settings</span>
      <svg width="12" height="20" viewBox="0 0 12 20"><path d="M2 2 L10 10 L2 18" stroke="#fff" stroke-width="2" fill="none"/></svg>
    </li>
  </ul>
</section>

<section class="screen screen--search" aria-label="Client search screen">
  <header class="app-header">
    <div class="brand"><span class="brand__mark"></span><span class="brand__name">VDN</span></div>
  </header>
  <div class="nav-bar">
    <svg width="10" height="16" viewBox="0 0 10 16"><path d="M8 1 L2 8 L8 15" stroke="#fff" stroke-width="2" fill="none"/></svg>
    <span class="nav-bar__title">Client Search</span>
    <svg width="14" height="14" viewBox="0 0 14 14"><circle cx="7" cy="7" r="6" stroke="#fff" stroke-width="1.5" fill="none"/><path d="M5 5.5 a2 2 0 1 1 2.6 1.9 c-.6.3-.6.7-.6 1.3" stroke="#fff" stroke-width="1.5" fill="none"/><circle cx="7" cy="10.5" r=".9" fill="#fff"/></svg>
  </div>
  <div class="search-form">
    <span class="search-field">First Name</span>
    <span class="search-field">Last Name</span>
    <span class="search-field">Client Id</span>
    <span class="search-field">DOB</span>
  </div>
  <div class="search-actions">
    <div class="status-toggle">
      <span class="status-toggle__active">Active</span>
      <span class="status-toggle__divider">|</span>
      <span class="status-toggle__inactive">InActive</span>
    </div>
    <span class="search-button">SEARCH</span>
  </div>

  <div class="results">
    <div class="results__head"><span>Client Name</span><span>Client ID</span><span>DOB</span></div>

    <div class="client-row">
      <span>Client A</span><span>123abc</span>
      <span class="client-dob">1/1/1979
        <svg width="14" height="8" viewBox="0 0 14 8"><rect x="0" y="1" width="3" height="6" fill="#fff"/><rect x="3" y="3.2" width="8" height="1.6" fill="#fff"/><rect x="11" y="1" width="3" height="6" fill="#fff"/></svg>
        <svg class="client-dob__toggle" width="8" height="6" viewBox="0 0 8 6"><path d="M1 5 L4 1.5 L7 5" stroke="#fff" stroke-width="1.3" fill="none"/></svg>
      </span>
    </div>
    <div class="client-detail">
      <div class="client-detail__summary">
        <span class="stars">136 <svg width="9" height="9" viewBox="0 0 10 10"><path d="M5 0.5 L6.3 3.6 L9.6 3.8 L7 6 L7.9 9.4 L5 7.6 L2.1 9.4 L3 6 L0.4 3.8 L3.7 3.6 Z" fill="#fff"/></svg></span>
        <span>Pain/Difficulty Graph</span>
      </div>
      <div class="prescription-head"><span>Issued</span><span>Expiration</span></div>
      <div class="prescription-row">
        <span>1/1/2019</span><span>2/1/2019</span>
        <span class="action-select">Actions<span class="action-select__arrow"><svg width="8" height="5" viewBox="0 0 8 5"><path d="M1 1 L4 4 L7 1" stroke="#111" stroke-width="1.4" fill="none"/></svg></span></span>
      </div>
      <div class="prescription-row">
        <span>12/1/2018</span><span>1/1/2019</span>
        <span class="action-select">Actions<span class="action-select__arrow"><svg width="8" height="5" viewBox="0 0 8 5"><path d="M1 1 L4 4 L7 1" stroke="#111" stroke-width="1.4" fill="none"/></svg></span></span>
      </div>
    </div>

    <div class="client-row">
      <span>Client B</span><span>245abc</span>
      <span class="client-dob">1/1/1969
        <svg width="14" height="8" viewBox="0 0 14 8"><rect x="0" y="1" width="3" height="6" fill="#fff"/><rect x="3" y="3.2" width="8" height="1.6" fill="#fff"/><rect x="11" y="1" width="3" height="6" fill="#fff"/></svg>
        <svg class="client-dob__toggle" width="8" height="6" viewBox="0 0 8 6"><path d="M1 1.5 L4 5 L7 1.5" stroke="#fff" stroke-width="1.3" fill="none"/></svg>
      </span>
    </div>
    <div class="client-row">
      <span>Client C</span><span>678abc</span>
      <span class="client-dob">1/1/1989
        <svg width="14" height="8" viewBox="0 0 14 8"><rect x="0" y="1" width="3" height="6" fill="#fff"/><rect x="3" y="3.2" width="8" height="1.6" fill="#fff"/><rect x="11" y="1" width="3" height="6" fill="#fff"/></svg>
        <svg class="client-dob__toggle" width="8" height="6" viewBox="0 0 8 6"><path d="M1 1.5 L4 5 L7 1.5" stroke="#fff" stroke-width="1.3" fill="none"/></svg>
      </span>
    </div>
    <div class="client-row">
      <span>Client D</span><span>901abc</span>
      <span class="client-dob">1/1/1989
        <svg width="14" height="8" viewBox="0 0 14 8"><rect x="0" y="1" width="3" height="6" fill="#fff"/><rect x="3" y="3.2" width="8" height="1.6" fill="#fff"/><rect x="11" y="1" width="3" height="6" fill="#fff"/></svg>
        <svg class="client-dob__toggle" width="8" height="6" viewBox="0 0 8 6"><path d="M1 1.5 L4 5 L7 1.5" stroke="#fff" stroke-width="1.3" fill="none"/></svg>
      </span>
    </div>
  </div>
</section>

</body>
</html>
```